Revamp our website

Our website needs a bit of a makeover as it is quite simple and not very interactive. Specific pages we would like to see renewed is the home page (www.kelpowerfield.com.au) , solutions top page (https://www.kelpowerfield.com.au/solutions/) and a detailed solution page (https://www.kelpowerfield.com.au/tundle-retail-final/)

The colour data lines are key to our branding and must be used (happy to see them being used in different ways).

```html
<!DOCTYPE html>
<html lang="en">
<head>
<meta charset="utf-8">
<title>Kelpower Field — Home</title>
<link href="https://fonts.googleapis.com/css2?family=Poppins:wght@300;400;500;600;700&display=swap" rel="stylesheet">
<style>
:root{
  --red:#c8163f;
  --red-dark:#a91034;
  --ink:#222;
  --body:#777;
  --soft:#f6f6f6;
  --line:#e6e6e6;
  --white:#fff;
}
*{box-sizing:border-box;margin:0;padding:0}
html,body{width:1200px;height:3273px;overflow:hidden}
body{font-family:"Poppins",sans-serif;color:var(--ink);background:var(--white);position:relative}
section,header,footer{position:absolute;left:0;width:1200px}
.center{text-align:center}
.eyebrow{font-size:10px;line-height:15px;letter-spacing:1.5px;color:var(--red);text-transform:uppercase;font-weight:500}
.heading{font-size:27px;line-height:36px;font-weight:500;color:var(--ink);margin-top:8px}
.rule{width:150px;height:1px;background:var(--red);opacity:.5;margin:12px auto 0}
.copy{font-size:13px;line-height:21px;color:var(--body)}
.btn{display:inline-block;font-size:10px;font-weight:600;letter-spacing:.8px;text-transform:uppercase;padding:0 16px;height:32px;line-height:32px}
.btn-red{background:var(--red);color:var(--white)}
.btn-outline-red{border:1px solid var(--red);color:var(--red)}

/* header */
.site-header{top:0;height:80px;background:var(--white)}
.brand{position:absolute;left:131px;top:8px;font-size:44px;font-weight:700;color:var(--red);letter-spacing:-1px}
.main-nav{position:absolute;left:380px;top:33px;display:flex;gap:40px;font-size:10px;font-weight:500;letter-spacing:.8px;text-transform:uppercase}
.main-nav .active{color:var(--red)}
.main-nav .active::before,.main-nav .active::after{content:"";display:inline-block;width:10px;height:1px;background:var(--red);vertical-align:middle;margin:0 5px}
.quote{position:absolute;left:938px;top:24px;height:32px;line-height:32px;padding:0 9px;font-size:10px}

/* hero */
.hero{top:80px;height:444px}
.hero-photo{position:absolute;inset:0;background:linear-gradient(100deg,#3b2e26 0%,#6b5646 35%,#4a3b31 60%,#2a2320 100%)}
.hero-shade{position:absolute;inset:0;background:rgba(0,0,0,.35)}
.hero-title{position:absolute;top:130px;width:100%;font-size:38px;font-weight:500;color:var(--white)}
.hero-sub{position:absolute;top:194px;width:100%;font-size:12px;line-height:21px;color:#eee}
.hero-actions{position:absolute;top:266px;width:100%;display:flex;justify-content:center;gap:22px}
.btn-ghost{border:1px solid var(--white);color:var(--white);display:flex;align-items:center;gap:8px}
.btn-white{background:var(--white);color:var(--red)}
.scroll-cue{position:absolute;left:592px;top:393px}

/* what we do */
.about{top:524px;height:408px;padding-top:70px}
.about .copy{width:730px;margin:28px auto 0;font-size:12px;line-height:20px}
.about .copy + .copy{margin-top:20px}
.about .btn{margin-top:30px}

/* solutions */
.solutions{top:932px;height:570px;background:var(--soft);padding-top:62px}
.solutions .copy{width:640px;margin:12px auto 0;font-size:12px;line-height:20px}
.solutions .lead{color:var(--red);font-weight:500}
.card-row{position:absolute;top:222px;left:155px;display:flex;gap:23px}
.solution-card{width:281px;height:290px;background:var(--white);text-align:center;padding-top:32px;box-shadow:0 2px 8px rgba(0,0,0,.05)}
.solution-card .icon{width:88px;height:88px;border-radius:50%;background:var(--red);margin:0 auto;display:flex;align-items:center;justify-content:center}
.solution-card h3{font-size:16px;line-height:24px;font-weight:500;margin-top:22px}
.solution-card p{font-size:12px;line-height:19px;color:var(--body);width:232px;margin:6px auto 0}
.solution-card .go{margin-top:14px;color:var(--red);font-size:18px;line-height:20px}
.solution-card.featured{background:var(--red)}
.solution-card.featured .icon{background:var(--white)}
.solution-card.featured h3,.solution-card.featured p,.solution-card.featured .go{color:var(--white)}

/* tundle band */
.tundle{top:1502px;height:468px}
.tundle-photo{position:absolute;inset:0;background:linear-gradient(110deg,#2e3a45 0%,#5b6670 40%,#7a6a58 70%,#3a3128 100%)}
.tundle-panel{position:absolute;left:240px;top:73px;width:720px;height:330px;background:rgba(255,255,255,.82);text-align:center;padding-top:40px}
.tundle-panel h2{font-size:31px;font-weight:500;color:var(--red)}
.tundle-panel .copy{width:640px;margin:30px auto 0;color:#555;font-size:12px;line-height:20px}
.tundle-panel .copy + .copy{margin-top:14px}
.tundle-panel .btn{margin-top:24px;height:30px;line-height:30px}

/* products */
.products{top:1970px;height:627px;padding-top:62px}
.product-row{position:absolute;top:147px;left:155px;display:flex;gap:23px}
.product-card{width:281px;height:340px;background:var(--white);text-align:center;box-shadow:0 2px 8px rgba(0,0,0,.07)}
.product-card .thumb{height:180px}
.product-card h3{font-size:16px;line-height:24px;font-weight:500;margin-top:20px}
.product-card p{font-size:12px;line-height:19px;color:var(--body);width:240px;margin:6px auto 0}
.product-card .go{margin-top:12px;color:var(--red);font-size:18px;line-height:20px}
.product-card.featured{background:var(--red)}
.product-card.featured h3,.product-card.featured p,.product-card.featured .go{color:var(--white)}
.product-nav{position:absolute;top:527px;width:100%;display:flex;justify-content:center;align-items:center;gap:22px;color:var(--red);font-size:16px}
.product-nav .btn{height:32px;line-height:30px;padding:0 36px}

/* philosophy */
.philosophy{top:2597px;height:396px;padding-top:58px}
.philosophy .copy{width:650px;margin:18px auto 0;font-size:12px;line-height:20px}
.client-name{margin-top:22px;font-size:13px;font-weight:500;color:var(--red)}
.client-org{font-size:12px;color:var(--ink);margin-top:2px}
.dots{display:flex;justify-content:center;gap:8px;margin-top:14px}
.dots span{width:6px;height:6px;border-radius:50%;background:#ddd}
.dots .on{background:var(--red)}
.avatar{position:absolute;border-radius:50%;border:3px solid var(--white);box-shadow:0 2px 6px rgba(0,0,0,.15)}

/* footer */
.site-footer{top:2993px;height:280px;background:var(--red);color:var(--white)}
.mailing{position:absolute;top:40px;left:79px;font-size:27px;font-weight:500}
.field{position:absolute;top:39px;height:42px;border:1px solid rgba(255,255,255,.8);font-size:11px;line-height:40px;padding-left:14px;color:#f4d6dd;width:217px}
.send{position:absolute;top:39px;left:1023px;width:98px;height:42px;background:var(--white);color:var(--red);font-size:10px;font-weight:600;text-align:center;line-height:42px;letter-spacing:.8px}
.footer-rule{position:absolute;top:112px;left:79px;width:1042px;height:1px;background:rgba(255,255,255,.3)}
.footer-brand{position:absolute;top:140px;left:79px;font-size:44px;font-weight:700;letter-spacing:-1px}
.footer-nav{position:absolute;top:160px;left:334px;display:flex;gap:28px;font-size:10px;font-weight:500;letter-spacing:.7px;text-transform:uppercase}
.social{position:absolute;top:149px;left:962px;display:flex;gap:11px}
.social span{width:32px;height:32px;border:1px solid rgba(255,255,255,.8)}
.social .on{background:var(--white)}
.footer-rule.low{top:213px}
.legal{position:absolute;top:236px;left:79px;font-size:10px}
.legal u{text-underline-offset:2px}
.legal-links{position:absolute;top:236px;right:79px;font-size:10px;letter-spacing:.7px}
.to-top{position:absolute;top:184px;left:1155px}
</style>
</head>
<body>

<header class="site-header">
  <div class="brand">kelpower</div>
  <nav class="main-nav">
    <span class="active">Home</span><span>About Us</span><span>Our Team</span><span>Solutions</span><span>Products</span><span>News</span>
  </nav>
  <span class="btn btn-red quote">Get a Free Quote</span>
</header>

<section class="hero">
  <div class="hero-photo" role="img" aria-label="Photo of a team laughing together around an office table"></div>
  <div class="hero-shade"></div>
  <h1 class="hero-title center">Fortune favours the Kelpower.</h1>
  <p class="hero-sub center">At Kelpower™, we develop software solutions that are specifically designed for<br>the Australian Utilities sector.</p>
  <div class="hero-actions">
    <span class="btn btn-ghost">
      <svg width="12" height="12" viewBox="0 0 24 24" fill="none" stroke="#fff" stroke-width="2"><path d="M5 3h4l2 5-3 2a12 12 0 0 0 6 6l2-3 5 2v4a2 2 0 0 1-2 2A18 18 0 0 1 3 5a2 2 0 0 1 2-2z"/></svg>
      61 3 9000 4120</span>
    <span class="btn btn-white">Explore More</span>
  </div>
  <svg class="scroll-cue" width="16" height="20" viewBox="0 0 16 20" fill="none" stroke="#fff" stroke-width="1.5"><path d="M8 2v15M3 12l5 5 5-5"/></svg>
</section>

<section class="about center">
  <div class="eyebrow">What We Do</div>
  <h2 class="heading">Welcome To Kelpower Field</h2>
  <div class="rule"></div>
  <p class="copy">At Kelpower™, we develop software solutions that are specifically designed for the Australian Utilities sector. Founded by two industry leaders 15 years ago, we are about making the lives easier for those who work so hard to meet growing business and consumer demands.</p>
  <p class="copy">Our solutions range from billing, data management, compliance, automation and revenue assurance through to complete end-to-end systems for Australian Retailers, Metering Services and Distribution.</p>
  <span class="btn btn-red">Discover More</span>
</section>

<section class="solutions center">
  <div class="eyebrow">Solutions</div>
  <h2 class="heading">We're Here For You.</h2>
  <div class="rule"></div>
  <p class="copy">Specialising in the Australian Utilities sector, we are driven to improve your operations<br>and customer experience through intelligent software.<br><span class="lead">Get started with Kelpower today.</span></p>
  <div class="card-row">
    <article class="solution-card">
      <div class="icon"><svg width="40" height="40" viewBox="0 0 40 40" fill="none" stroke="#fff" stroke-width="2"><path d="M6 20 20 8l14 12M10 17v15h20V17M17 32v-8h6v8"/></svg></div>
      <h3>Retail</h3>
      <p>Are you looking to improve your bottom line by minimising operational costs...</p>
      <div class="go">→</div>
    </article>
    <article class="solution-card featured">
      <div class="icon"><svg width="40" height="40" viewBox="0 0 40 40" fill="none" stroke="#c8163f" stroke-width="2"><circle cx="20" cy="20" r="14"/><path d="M20 20l7-6M12 24h16"/></svg></div>
      <h3>Metering Services</h3>
      <p>Do you have missing or incorrect data that is impacting your Service Level Agreements with customers...</p>
      <div class="go">→</div>
    </article>
    <article class="solution-card">
      <div class="icon"><svg width="40" height="40" viewBox="0 0 40 40" fill="none" stroke="#fff" stroke-width="2"><circle cx="20" cy="13" r="3"/><path d="M13 7a10 10 0 0 0 0 12M27 7a10 10 0 0 1 0 12M20 16l-7 18M20 16l7 18M15 28h10"/></svg></div>
      <h3>Distribution &amp; Transmission</h3>
      <p>Do you have a complex environment that involves a variety of tariffs at one time...</p>
      <div class="go">→</div>
    </article>
  </div>
</section>

<section class="tundle">
  <div class="tundle-photo" role="img" aria-label="Photo of colleagues working together on a laptop"></div>
  <div class="tundle-panel">
    <h2>Tundle My Friend, Tundle.</h2>
    <p class="copy">Tundle is a suite of products combined to create end-to-end software solutions for Australian utility participants.</p>
    <p class="copy">Tundle revolutionises the way you conduct business by bringing greater efficiency and transparency to your day-to-day operations.</p>
    <span class="btn btn-outline-red">Read More</span>
  </div>
</section>

<section class="products center">
  <div class="eyebrow">Products</div>
  <h2 class="heading">Our Products</h2>
  <div class="rule"></div>
  <div class="product-row">
    <article class="product-card">
      <div class="thumb" role="img" aria-label="Photo of paper invoices and a calculator" style="background:linear-gradient(135deg,#e8e6e2,#a9a39b)"></div>
      <h3>Billing</h3>
      <p>Improve and automate your number one business process, no matter how flexible or complex the...</p>
      <div class="go">→</div>
    </article>
    <article class="product-card featured">
      <div class="thumb" role="img" aria-label="Photo of a laptop showing compliance on a desk" style="background:linear-gradient(135deg,#d9b36a,#5d6f86)"></div>
      <h3>Compliance &amp; Automation</h3>
      <p>Compliance requirements in the Australian market continue to grow in complexity.</p>
      <div class="go">→</div>
    </article>
    <article class="product-card">
      <div class="thumb" role="img" aria-label="Photo of a team reviewing reports at a table" style="background:linear-gradient(135deg,#cfcac2,#6f6a63)"></div>
      <h3>Revenue Assurance</h3>
      <p>Protect your bottom line with Kelpower. With the only Australian software products that are dedicated to...</p>
      <div class="go">→</div>
    </article>
  </div>
  <div class="product-nav"><span>←</span><span class="btn btn-outline-red">View All</span><span>→</span></div>
</section>

<section class="philosophy center">
  <div class="eyebrow">Happy Clients</div>
  <h2 class="heading">Our Kelpower Philosophy.</h2>
  <p class="copy">Lorem Ipsum is simply dummy text of the printing and typesetting industry. Lorem Ipsum has been the industry's standard dummy text ever since the 1500s, when an unknown printer took a galley of type and scrambled it to make a type specimen book. It has survived not only five centuries, but also the leap into electronic typesetting, remaining essentially unchanged.</p>
  <div class="client-name">Marcus Dell</div>
  <div class="client-org">Northgate Power Co</div>
  <div class="dots"><span></span><span class="on"></span><span></span></div>
  <span class="avatar" role="img" aria-label="Client portrait" style="left:100px;top:118px;width:70px;height:70px;background:#c9a58c"></span>
  <span class="avatar" role="img" aria-label="Client portrait" style="left:183px;top:205px;width:34px;height:34px;background:#8a7a6c"></span>
  <span class="avatar" role="img" aria-label="Client portrait" style="left:82px;top:241px;width:62px;height:62px;background:#5a4d44"></span>
  <span class="avatar" role="img" aria-label="Client portrait" style="left:244px;top:270px;width:26px;height:26px;background:#9b8b7e"></span>
  <span class="avatar" role="img" aria-label="Client portrait" style="left:1030px;top:118px;width:70px;height:70px;background:#7a5c4a"></span>
  <span class="avatar" role="img" aria-label="Client portrait" style="left:982px;top:205px;width:34px;height:34px;background:#4e4540"></span>
  <span class="avatar" role="img" aria-label="Client portrait" style="left:1056px;top:241px;width:62px;height:62px;background:#b09482"></span>
  <span class="avatar" role="img" aria-label="Client portrait" style="left:930px;top:270px;width:26px;height:26px;background:#6b5f57"></span>
</section>

<footer class="site-footer">
  <div class="mailing">Join Our Mailing List</div>
  <div class="field" style="left:545px">Enter Your Name...</div>
  <div class="field" style="left:783px">Enter Your Email...</div>
  <div class="send">SEND →</div>
  <div class="footer-rule"></div>
  <div class="footer-brand">kelpower</div>
  <nav class="footer-nav"><span>Home</span><span>About Us</span><span>Our Team</span><span>Solutions</span><span>Products</span><span>News</span><span>Contact Us</span></nav>
  <div class="social"><span class="on"></span><span></span><span></span><span></span></div>
  <svg class="to-top" width="12" height="16" viewBox="0 0 12 16" fill="none" stroke="#fff" stroke-width="1.5"><path d="M6 15V2M1 7l5-5 5 5"/></svg>
  <div class="footer-rule low"></div>
  <div class="legal">© 2018 <u>Kelpower Field Pvt Ltd</u>. All rights reserved.</div>
  <div class="legal-links">PRIVACY POLICY &nbsp;|&nbsp; LEGAL NOTICES</div>
</footer>

</body>
</html>
```